Email signature design - law firm

We are a small boutique law firm which is located near the beach in Manly, Australia.

We have just recently developed a new logo and are looking to redesign our letterhead, business cards and email signatures.

This brief is for our email signatures. This is an email signature to appear at the bottom of our Outlook emails so we would like it to be text that we are able to edit as the wording in our email signature often required amendments.

I have attached a word document which had our new logo, and our previous email signature which all the information/wording that needs to be included.

We would like multiple designs with a modern, simplistic yet striking look.

Thanks.

font - raleway or montserrat

Need extra days to review

• Must have the exact wording which appears in the email signature in the word document attached to brief.
• Must be able to edit the text as it is for an Outlook email signature which wording will change from time to time.

```html
<!DOCTYPE html>
<html lang="en">
<head>
<meta charset="utf-8">
<title>Email Signature – Harlow &amp; Partners</title>
<link href="https://fonts.googleapis.com/css2?family=Raleway:wght@600;700;800&family=Lato:wght@400;700&display=swap" rel="stylesheet">
<style>
  :root {
    --page-bg: #f2f2f2;
    --card-bg: #ffffff;
    --brand-blue: #5562a8;
    --rule-navy: #3d4a8f;
    --ink: #1e1e1e;
    --brand-gold: #c2a86e;
  }
  * { margin: 0; padding: 0; box-sizing: border-box; }
  html, body {
    width: 1200px;
    height: 757px;
    overflow: hidden;
    background: var(--page-bg);
  }
  .signature {
    position: absolute;
    left: 50px;
    top: 190px;
    width: 1100px;
    height: 377px;
    background: var(--card-bg);
    font-family: "Lato", Arial, sans-serif;
    color: var(--ink);
  }
  .firm-mark {
    position: absolute;
    left: 64px;
    top: 60px;
    width: 347px;
    display: flex;
    flex-direction: column;
    align-items: center;
    gap: 26px;
  }
  .firm-mark__dot {
    width: 110px;
    height: 110px;
    border-radius: 50%;
    background: var(--brand-blue);
  }
  .firm-mark__name {
    font-family: "Raleway", Arial, sans-serif;
    font-weight: 700;
    font-size: 31px;
    letter-spacing: 1px;
    color: var(--ink);
    white-space: nowrap;
  }
  .contact {
    position: absolute;
    right: 36px;
    top: 72px;
    text-align: right;
  }
  .contact__name {
    font-family: "Raleway", Arial, sans-serif;
    font-weight: 800;
    font-size: 36px;
    line-height: 44px;
    color: var(--brand-blue);
  }
  .contact__title {
    font-size: 26px;
    line-height: 30px;
  }
  .contact__details {
    margin-top: 52px;
    font-size: 25px;
    line-height: 36px;
  }
  .contact__label {
    font-weight: 700;
    color: var(--brand-blue);
  }
  .signature__rule {
    position: absolute;
    left: 23px;
    right: 21px;
    top: 308px;
    height: 3px;
    background: var(--rule-navy);
  }
  .signature__web {
    position: absolute;
    left: 0;
    right: 0;
    top: 326px;
    text-align: center;
    font-weight: 700;
    font-size: 25px;
    color: var(--brand-blue);
  }
</style>
</head>
<body>
  <div class="signature">
    <div class="firm-mark">
      <div class="firm-mark__dot"></div>
      <div class="firm-mark__name">Harlow &amp; Partners</div>
    </div>

    <div class="contact">
      <div class="contact__name">MEGAN LAWSON</div>
      <div class="contact__title">Practise Manager</div>
      <div class="contact__details">
        <div><span class="contact__label">P:</span> (02) 5550 1234</div>
        <div><span class="contact__label">E:</span> megan.lawson@harlowpartners.com.au</div>
      </div>
    </div>

    <div class="signature__rule"></div>
    <div class="signature__web">www.harlowpartners.com.au</div>
  </div>
</body>
</html>
```